Oil and Gas Exploration and Production company needs a business card design

We need a business card design using our logo and colors in the logo. We want a mainstream design.

```html
<!DOCTYPE html>
<html lang="en">
<head>
<meta charset="utf-8">
<title>Tavira Oil &amp; Gas — Business Card</title>
<link rel="stylesheet" href="https://fonts.googleapis.com/css2?family=Work+Sans:wght@400;500;600&display=swap">
<style>
  :root {
    --backdrop: #2a2a2b;
    --card: #1d1d1e;
    --card-edge: #262627;
    --ink: #f1f1f1;
    --ink-soft: #d8d8d8;
    --brand-grey: #c9c9c9;
    --gold: #e0a526;
  }
  * { margin: 0; padding: 0; box-sizing: border-box; }
  html, body {
    width: 1200px; height: 900px; overflow: hidden;
    background: var(--backdrop);
    font-family: "Work Sans", Arial, sans-serif;
  }
  .canvas {
    position: relative; width: 1200px; height: 900px;
  }
  .card {
    position: absolute; left: 260px; width: 680px; height: 390px;
    background: linear-gradient(135deg, var(--card) 0%, var(--card-edge) 100%);
    box-shadow: 0 10px 30px rgba(0,0,0,0.45);
  }
  .card--front { top: 40px; }
  .card--back { top: 470px; }

  .brand {
    display: flex; align-items: center; gap: 14px;
    color: var(--brand-grey);
    font-weight: 600; font-size: 40px; letter-spacing: 0.01em;
    white-space: nowrap;
  }
  .brand__dot {
    width: 26px; height: 26px; border-radius: 50%;
    background: var(--brand-grey); flex: none;
  }
  .card--front .brand {
    position: absolute; left: 0; right: 0; top: 0; bottom: 0;
    justify-content: center;
  }
  .card--back .brand {
    position: absolute; left: 40px; top: 168px; font-size: 30px; gap: 10px;
  }
  .card--back .brand__dot { width: 20px; height: 20px; }

  .divider {
    position: absolute; left: 352px; top: 100px;
    width: 3px; height: 190px; background: var(--gold);
  }
  .contact {
    position: absolute; left: 390px; top: 96px; color: var(--ink);
  }
  .contact__name {
    color: var(--gold); font-weight: 500; font-size: 30px; line-height: 1.1;
  }
  .contact__role {
    font-size: 16px; color: var(--ink-soft); margin-top: 2px;
  }
  .contact__address {
    font-size: 17px; line-height: 1.35; margin-top: 18px; color: var(--ink-soft);
  }
  .contact__list { list-style: none; margin-top: 14px; }
  .contact__item {
    display: flex; align-items: center; gap: 10px;
    font-size: 18px; line-height: 1.45; color: var(--ink);
  }
  .contact__icon { width: 12px; height: 12px; flex: none; }
  .contact__domain { color: var(--gold); }
</style>
</head>
<body>
<main class="canvas">
  <section class="card card--front" aria-label="Card front">
    <div class="brand"><span class="brand__dot"></span>Tavira Oil &amp; Gas</div>
  </section>

  <section class="card card--back" aria-label="Card back">
    <div class="brand"><span class="brand__dot"></span>Tavira Oil &amp; Gas</div>
    <div class="divider"></div>
    <div class="contact">
      <p class="contact__name">Dale Whitford</p>
      <p class="contact__role">CFO</p>
      <p class="contact__address">2450 W Prairie Ave,<br>Midland, Texas us</p>
      <ul class="contact__list">
        <li class="contact__item">
          <svg class="contact__icon" viewBox="0 0 12 12" aria-hidden="true"><path d="M2.5 1 L4.5 1 L5 3.5 L3.8 4.4 Q4.8 6.8 7.6 8.2 L8.5 7 L11 7.5 L11 9.5 Q10.5 11 9 11 Q1 9.5 1 2.5 Q1 1 2.5 1 Z" fill="var(--gold)"/></svg>
          (555) 410-2287
        </li>
        <li class="contact__item">
          <svg class="contact__icon" viewBox="0 0 12 12" aria-hidden="true"><rect x="0.75" y="2.25" width="10.5" height="7.5" fill="none" stroke="var(--gold)" stroke-width="1.2"/><path d="M1 2.6 L6 6.5 L11 2.6" fill="none" stroke="var(--gold)" stroke-width="1.2"/></svg>
          info@taviraoilgas.com
        </li>
        <li class="contact__item">
          <svg class="contact__icon" viewBox="0 0 12 12" aria-hidden="true"><circle cx="6" cy="6" r="5.2" fill="none" stroke="var(--gold)" stroke-width="1.1"/><ellipse cx="6" cy="6" rx="2.2" ry="5.2" fill="none" stroke="var(--gold)" stroke-width="1"/><path d="M1 6 H11" stroke="var(--gold)" stroke-width="1"/></svg>
          <span>www.<span class="contact__domain">taviraoilgas</span>.com</span>
        </li>
      </ul>
    </div>
  </section>
</main>
</body>
</html>
```